Top of the line business card design needed for real estate brokerage

We currently have a business card with our logo but would like to have a revised version. We would love for you to implement your own design that will catch anyone's attention. The theme colors should be black, royal blue, gray/silver, and white.The contact information should be the same as the info on our current business card (picture attached). In the design that we pick, we will need to be able to edit the text so that we can customize the text content for each of our agents. Same goes for the professional picture. There should be an area on the card that each agent can have their professional portrait attached. Please include a version without the picture option as well for agents that do not wish to have a professional picture attached.

```html
<!DOCTYPE html>
<html lang="en">
<head>
<meta charset="utf-8">
<title>Clear Harbor Realty – Business Cards</title>
<link href="https://fonts.googleapis.com/css2?family=Open+Sans:ital,wght@0,400;0,600;0,800;1,400&display=swap" rel="stylesheet">
<style>
  :root {
    --royal: #1f4fb3;
    --ink: #1d1d1f;
    --silver: #a9abae;
    --silver-light: #dcdde0;
    --paper: #ffffff;
    --backdrop: #e9e9eb;
  }
  * { box-sizing: border-box; margin: 0; padding: 0; }
  html, body { width: 848px; height: 1200px; overflow: hidden; }
  body {
    background: var(--backdrop);
    font-family: "Open Sans", Arial, sans-serif;
    color: var(--ink);
    position: relative;
  }
  .card {
    position: absolute;
    width: 300px;
    height: 525px;
    background: var(--paper);
    box-shadow: 0 2px 10px rgba(0,0,0,.12);
  }
  .card--front-plain { left: 100px; top: 45px; }
  .card--back-plain  { left: 448px; top: 45px; }
  .card--front-services { left: 100px; top: 630px; }
  .card--back-portrait  { left: 448px; top: 630px; }

  /* brand block */
  .brand-art {
    position: absolute;
    border-radius: 4px;
    background: linear-gradient(180deg, #eef0f3 0%, #cfd2d8 55%, #b4c2e2 100%);
  }
  .brand-name {
    position: absolute;
    display: flex;
    align-items: center;
    gap: 8px;
    font-weight: 800;
    color: var(--ink);
    white-space: nowrap;
  }
  .brand-name .mark {
    width: 14px; height: 14px; background: var(--royal); flex: none;
  }
  .card--front-plain .brand-art { left: 40px; top: 130px; width: 220px; height: 170px; }
  .card--front-plain .brand-name { left: 50px; top: 310px; font-size: 21px; }
  .card--front-services .brand-art { left: 40px; top: 60px; width: 220px; height: 160px; }
  .card--front-services .brand-name { left: 50px; top: 230px; font-size: 21px; }

  /* person */
  .person { position: absolute; left: 0; width: 100%; text-align: center; }
  .person__name {
    color: var(--royal); font-weight: 800; font-size: 22px; letter-spacing: 1.5px; line-height: 1.1;
  }
  .person__role { color: var(--royal); font-style: italic; font-size: 11px; }

  .contact { position: absolute; left: 38px; font-size: 11.5px; line-height: 1.4; }
  .contact__address { margin-bottom: 14px; }
  .contact__row { display: flex; align-items: center; gap: 8px; margin-bottom: 2px; font-size: 12.5px; }
  .contact__row svg { width: 11px; height: 11px; flex: none; fill: var(--ink); }

  .rule { position: absolute; left: 30px; right: 30px; height: 1.5px; background: var(--royal); }

  .services { position: absolute; list-style: none; color: var(--royal); font-size: 13px; line-height: 1.9; }
  .services--slashed li::before { content: "/"; margin-right: 8px; }

  .card--back-plain .person { top: 40px; }
  .card--back-plain .contact { top: 105px; }
  .card--back-plain .rule { top: 265px; }
  .card--back-plain .brand-art { left: 25px; top: 300px; width: 110px; height: 75px; }
  .card--back-plain .brand-name { left: 25px; top: 382px; font-size: 11px; gap: 5px; }
  .card--back-plain .brand-name .mark { width: 9px; height: 9px; }
  .card--back-plain .services { left: 150px; top: 295px; font-size: 12.5px; }

  .card--front-services .services { left: 50px; top: 300px; }

  .portrait {
    position: absolute; left: 75px; top: 40px; width: 150px; height: 150px; border-radius: 50%;
    background: radial-gradient(circle at 50% 40%, #d9d6d2 0%, #b9b3ad 55%, #7d7670 100%);
  }
  .card--back-portrait .person { top: 210px; }
  .card--back-portrait .contact { top: 275px; }
</style>
</head>
<body>
  <svg width="0" height="0" style="position:absolute">
    <defs>
      <symbol id="icon-phone" viewBox="0 0 12 12"><path d="M2.5 0.5l2 2.2-1 1.3c.6 1.6 1.9 2.9 3.5 3.5l1.3-1 2.2 2-1.1 2C5.3 10.3 1.7 6.7 .5 1.6z"/></symbol>
      <symbol id="icon-mail" viewBox="0 0 12 12"><path d="M0 2h12v8H0z M0 2l6 4.5L12 2" /><path d="M0 2l6 4.5L12 2z" fill="#fff"/></symbol>
      <symbol id="icon-web" viewBox="0 0 12 12"><circle cx="6" cy="6" r="5.5"/><path d="M.5 6h11M6 .5v11M2 3h8M2 9h8" stroke="#fff" stroke-width=".9" fill="none"/></symbol>
    </defs>
  </svg>

  <section class="card card--front-plain">
    <div class="brand-art" role="img" aria-label="Grey city skyline with blue rooftop illustration"></div>
    <div class="brand-name"><span class="mark"></span>Clear Harbor Realty</div>
  </section>

  <section class="card card--back-plain">
    <div class="person">
      <p class="person__name">Marcus Delacroix</p>
      <p class="person__role">Broker</p>
    </div>
    <div class="contact">
      <p class="contact__address">2400 Harbor View Ave, Suite 310<br>Palm Shores, FL 33400</p>
      <p class="contact__row"><svg><use href="#icon-phone"/></svg>555 - 014 - 2287</p>
      <p class="contact__row"><svg><use href="#icon-mail"/></svg>marcus@clearharborrealty.com</p>
      <p class="contact__row"><svg><use href="#icon-web"/></svg>clearharborrealty.com</p>
    </div>
    <div class="rule"></div>
    <div class="brand-art" role="img" aria-label="Small skyline with blue rooftop illustration"></div>
    <div class="brand-name"><span class="mark"></span>Clear Harbor Realty</div>
    <ul class="services">
      <li>Residential Real Estate</li>
      <li>Commercial Real Estate</li>
      <li>Property Management</li>
      <li>Invesments</li>
    </ul>
  </section>

  <section class="card card--front-services">
    <div class="brand-art" role="img" aria-label="Grey city skyline with blue rooftop illustration"></div>
    <div class="brand-name"><span class="mark"></span>Clear Harbor Realty</div>
    <ul class="services services--slashed">
      <li>Residential Real Estate</li>
      <li>Commercial Real Estate</li>
      <li>Property Management</li>
      <li>Invesments</li>
    </ul>
  </section>

  <section class="card card--back-portrait">
    <div class="portrait" role="img" aria-label="Agent's professional portrait"></div>
    <div class="person">
      <p class="person__name">Marcus Delacroix</p>
      <p class="person__role">Broker</p>
    </div>
    <div class="contact">
      <p class="contact__address">2400 Harbor View Ave, Suite 310<br>Palm Shores, FL 33400</p>
      <p class="contact__row"><svg><use href="#icon-phone"/></svg>555 - 014 - 2287</p>
      <p class="contact__row"><svg><use href="#icon-mail"/></svg>marcus@clearharborrealty.com</p>
      <p class="contact__row"><svg><use href="#icon-web"/></svg>clearharborrealty.com</p>
    </div>
  </section>
</body>
</html>
```